Business Card - Cooperate

Business Card for Larkfield Management Consulting

Target Market(s)

Corparte - b2B

Industry/Entity Type

Management Consulting - Professional Services

Contact Information for Business Card

Company Name , Slogan , Dummy Address,

Requirements
Must have
• Reach your Full Potential

```html
<!DOCTYPE html>
<html lang="en">
<head>
<meta charset="utf-8">
<title>Larkfield Management Consulting – Business Card</title>
<link href="https://fonts.googleapis.com/css2?family=Montserrat:wght@400;500;600;700;800&display=swap" rel="stylesheet">
<style>
  :root {
    --canvas: #e6e7ea;
    --navy: #2b3a8c;
    --navy-deep: #2f3f78;
    --green: #5aa64a;
    --green-bright: #7bbf3a;
    --teal: #3f9d8a;
    --band-blue: #3d78b0;
    --white: #ffffff;
    --text-dark: #2c2f45;
  }
  * { box-sizing: border-box; margin: 0; padding: 0; }
  html, body { width: 1200px; height: 900px; overflow: hidden; }
  body {
    background: var(--canvas);
    font-family: "Montserrat", sans-serif;
    display: flex;
    flex-direction: column;
    align-items: center;
    justify-content: center;
    gap: 40px;
  }
  .card {
    width: 640px;
    height: 366px;
    border-radius: 18px;
    position: relative;
    overflow: hidden;
    box-shadow: 0 10px 30px rgba(0,0,0,0.15);
  }

  /* Front */
  .card-front {
    background: linear-gradient(30deg, var(--green) 0%, #437d5e 45%, var(--navy-deep) 100%);
    display: flex;
    align-items: center;
    justify-content: center;
  }
  .brand { display: flex; align-items: center; gap: 22px; }
  .brand-dot { border-radius: 50%; flex-shrink: 0; }
  .brand-text { display: flex; flex-direction: column; }
  .brand-name { font-weight: 700; line-height: 1; letter-spacing: -1px; text-transform: lowercase; }
  .brand-slogan { font-weight: 700; text-transform: uppercase; letter-spacing: 3px; margin-top: 8px; }

  .card-front .brand-dot { width: 92px; height: 92px; background: var(--white); }
  .card-front .brand-name { font-size: 84px; color: var(--white); }
  .card-front .brand-slogan { font-size: 13px; color: var(--white); }

  /* Back */
  .card-back { background: var(--white); }
  .card-back .brand { position: absolute; left: 44px; top: 40px; gap: 16px; }
  .card-back .brand-dot { width: 62px; height: 62px; background: var(--navy); }
  .card-back .brand-name { font-size: 56px; color: var(--navy); }
  .card-back .brand-slogan { font-size: 9.5px; color: var(--teal); letter-spacing: 2.4px; }

  .person { position: absolute; left: 44px; top: 170px; }
  .person-name { font-size: 26px; font-weight: 800; color: var(--navy); }
  .person-role { font-size: 14px; font-weight: 500; color: var(--text-dark); margin-top: 2px; }
  .divider { width: 16px; height: 2px; background: var(--green-bright); margin: 14px 0 12px; }

  .contact-list { list-style: none; display: flex; flex-direction: column; gap: 7px; }
  .contact-item { display: flex; align-items: center; gap: 12px; font-size: 13.5px; color: var(--text-dark); }
  .contact-icon { width: 13px; height: 13px; flex-shrink: 0; }

  .address-band {
    position: absolute; left: 0; right: 0; bottom: 0; height: 44px;
    background: linear-gradient(90deg, var(--green-bright) 0%, #4f9f6e 50%, var(--band-blue) 100%);
    display: flex; align-items: center; padding-left: 44px;
    color: var(--white); font-size: 13.5px; font-weight: 500;
  }
</style>
</head>
<body>

<section class="card card-front" aria-label="Card front">
  <div class="brand">
    <span class="brand-dot"></span>
    <div class="brand-text">
      <span class="brand-name">larkfield</span>
      <span class="brand-slogan">Reach your full potential</span>
    </div>
  </div>
</section>

<section class="card card-back" aria-label="Card back">
  <div class="brand">
    <span class="brand-dot"></span>
    <div class="brand-text">
      <span class="brand-name">larkfield</span>
      <span class="brand-slogan">Reach your full potential</span>
    </div>
  </div>

  <div class="person">
    <p class="person-name">Jordan Ellery</p>
    <p class="person-role">President</p>
    <div class="divider"></div>
    <ul class="contact-list">
      <li class="contact-item">
        <svg class="contact-icon" viewBox="0 0 24 24"><path fill="#7bbf3a" d="M6.6 10.8a15 15 0 0 0 6.6 6.6l2.2-2.2a1 1 0 0 1 1-.25 11.4 11.4 0 0 0 3.6.57 1 1 0 0 1 1 1V20a1 1 0 0 1-1 1A17 17 0 0 1 3 4a1 1 0 0 1 1-1h3.5a1 1 0 0 1 1 1c0 1.25.2 2.45.57 3.57a1 1 0 0 1-.25 1z"/></svg>
        <span>1-555-214-3087</span>
      </li>
      <li class="contact-item">
        <svg class="contact-icon" viewBox="0 0 24 24"><path fill="#7bbf3a" d="M2 5h20v14H2z"/><path fill="none" stroke="#fff" stroke-width="2" d="M2 5l10 8 10-8"/></svg>
        <span>info@yourmail.com</span>
      </li>
      <li class="contact-item">
        <svg class="contact-icon" viewBox="0 0 24 24"><circle cx="12" cy="12" r="10" fill="#7bbf3a"/><path fill="none" stroke="#fff" stroke-width="1.6" d="M2 12h20M12 2c3 3 3 17 0 20M12 2c-3 3-3 17 0 20"/></svg>
        <span>www.yourdomain.com</span>
      </li>
    </ul>
  </div>

  <div class="address-band">Here is your Address Road no. #32, Texas</div>
</section>

</body>
</html>
```